Create modern and sleek business card for luxury real estate company

We're a "boutique" real estate office looking for a design that gets across a highly modern luxury brand. Blacks and whites are probably the best colors unless we try a silver foil for the logo. I've attached a version of our current logo here. I'd like to swap out the current font on there with Gotham Light Regular.

I'm looking to have one side of the card have the logo with the space for our agents info on the other side.

Target Market(s)

Young professionals in a "luxury" headspace

Industry/Entity Type

Real estate

Contact Information for Business Card

A place for agent name, cell number, website. The slogan "Purely Reimagining Property".

Font styles to use
Other font styles liked:
• Gotham Regular

Colors

Designer to choose only greyscale colors for use in the design.

Requirements
Must have
• Matte black as the background color. Clean lines and use of contrast. A specific design aspect that will use silver foil.
Nice to have
• Up in the air on integrating a QR code
Should not have
• Any houses or other real estate related design (ex: a clip art house)

```html
<!DOCTYPE html>
<html lang="en">
<head>
<meta charset="utf-8">
<title>Lumen Realty Business Card</title>
<link href="https://fonts.googleapis.com/css2?family=Montserrat:wght@300;400;700&display=swap" rel="stylesheet">
<style>
  :root {
    --band-light: #a6a6a6;
    --card-black: #2b2a2c;
    --card-white: #ffffff;
    --ink: #231f20;
    --silver: #f1f1f1;
    --dash: #1a191b;
  }
  html, body { margin: 0; padding: 0; overflow: hidden; }
  .canvas {
    position: relative;
    width: 1200px;
    height: 960px;
    overflow: hidden;
    background: var(--band-light);
    font-family: "Montserrat", sans-serif;
  }
  .backdrop { position: absolute; inset: 0; }
  .card { position: absolute; width: 476px; overflow: hidden; }
  .card--front { left: 362px; top: 168px; height: 285px; background: var(--card-black); }
  .card--back { left: 361px; top: 481px; height: 284px; background: var(--card-white); }

  .front__frame {
    position: absolute;
    left: 32px; top: 31px;
    width: 412px; height: 222px;
    border: 1px dashed var(--dash);
  }
  .brand__circle {
    position: absolute;
    left: 196px; top: 72px;
    width: 84px; height: 84px;
    border: 3px solid var(--silver);
    border-radius: 50%;
    box-sizing: border-box;
  }
  .brand__rule {
    position: absolute;
    height: 1px;
    background: var(--silver);
  }
  .brand__rule--left { left: 122px; top: 158px; width: 87px; }
  .brand__rule--right { left: 273px; top: 158px; width: 87px; }
  .brand__rule--under { left: 122px; top: 205px; width: 233px; }
  .brand__name {
    position: absolute;
    left: 122px; width: 238px; top: 170px;
    text-align: center;
    color: var(--silver);
    font-weight: 300;
    font-size: 25px;
    line-height: 30px;
    letter-spacing: 0.5px;
    white-space: nowrap;
  }

  .slogan__word {
    position: absolute;
    left: 40px; top: 44px;
    margin: 0;
    font-weight: 300;
    font-size: 46px;
    line-height: 1;
    letter-spacing: 3px;
    color: var(--ink);
  }
  .slogan__tagline {
    position: absolute;
    left: 45px; top: 118px;
    font-size: 6.5px;
    letter-spacing: 1.6px;
    color: var(--ink);
    white-space: nowrap;
  }
  .agent {
    position: absolute;
    right: 44px; top: 173px;
    text-align: right;
    color: var(--ink);
  }
  .agent__name {
    display: inline-block;
    font-weight: 700;
    font-size: 19px;
    letter-spacing: 0.8px;
    margin: 0;
    padding-bottom: 6px;
    position: relative;
  }
  .agent__name::after {
    content: "";
    position: absolute;
    right: 0; bottom: 0;
    width: 62px; height: 1px;
    background: var(--ink);
  }
  .agent__line {
    margin: 0;
    font-weight: 300;
    font-size: 13px;
    letter-spacing: 1.4px;
    line-height: 21px;
  }
  .agent__line:first-of-type { margin-top: 6px; }
  .back__bar {
    position: absolute;
    left: 444px; top: 182px;
    width: 32px; height: 71px;
    background: var(--ink);
  }
</style>
</head>
<body>
<div class="canvas">
  <svg class="backdrop" width="1200" height="960" viewBox="0 0 1200 960" aria-hidden="true">
    <defs>
      <linearGradient id="upperShade" x1="0" y1="0" x2="1" y2="1">
        <stop offset="0" stop-color="#616161"/>
        <stop offset="0.5" stop-color="#959595"/>
        <stop offset="1" stop-color="#7a7a7a"/>
      </linearGradient>
      <linearGradient id="lowerShade" x1="0" y1="0" x2="1" y2="1">
        <stop offset="0" stop-color="#9a9a9a"/>
        <stop offset="0.5" stop-color="#777777"/>
        <stop offset="1" stop-color="#646464"/>
      </linearGradient>
    </defs>
    <rect width="1200" height="960" fill="#a6a6a6"/>
    <polygon points="0,0 771,0 0,771" fill="url(#upperShade)"/>
    <polygon points="1200,189 1200,960 429,960" fill="url(#lowerShade)"/>
  </svg>

  <section class="card card--front" aria-label="Card front">
    <div class="front__frame"></div>
    <div class="brand__circle"></div>
    <div class="brand__rule brand__rule--left"></div>
    <div class="brand__rule brand__rule--right"></div>
    <div class="brand__name">LUMEN REALTY</div>
    <div class="brand__rule brand__rule--under"></div>
  </section>

  <section class="card card--back" aria-label="Card back">
    <h1 class="slogan__word">Purely</h1>
    <div class="slogan__tagline">Reimagining Property</div>
    <div class="agent">
      <h2 class="agent__name">Adrian Vale</h2>
      <p class="agent__line">555-0142-018</p>
      <p class="agent__line">lumenrealty.com</p>
    </div>
    <div class="back__bar"></div>
  </section>
</div>
</body>
</html>
```